Flyer for Brightwell Table Provisions Company

Flyer Size: Double Sided 210mm * 148mm (Half a Sheet of Paper)
For your reference I have attached the logo and the web address is www.brightwelltableprovisions.com.
Specifications:
- Must contain the menu pricing chart, contact information, and hours of operation posted on the website.
- The menu must have an organization system from 1. Select Glaze through 4.Drinks. This will be the determining factor for selection. Graphic must be a mixture of creativity and function.
-The flyer can be identical on both sides (Not a determining factor)
-Incorporate the logo on both sides.
-The flyer does not have to be based on the website. (Not a determining factor)
My team will be handing these flyers out to HR Directors and Securities at Corporate offices.
Please let me know if you have any questions.
Updates
Project Deadline Extended
Reason: Website was not operational .
Brief has been updated and the website is up for your reference.
Target Market(s)
Corporate Office Catering. Secretary or HR director, usually a female.
Industry/Entity Type
Catering
Look and feel

```html
<!DOCTYPE html>
<html lang="en">
<head>
<meta charset="utf-8">
<title>Brightwell Table Provisions – Flyer</title>
<link href="https://fonts.googleapis.com/css2?family=Source+Sans+3:wght@400;600;700&display=swap" rel="stylesheet">
<style>
  :root {
    --stage: #1d1612;
    --paper: #110806;
    --paper-glow: #2a1209;
    --brand: #f0461c;
    --accent: #e3302a;
    --muted: #8c8480;
    --rule: #6a2018;
    --table-rule: #4a403c;
    --footer: #050302;
  }
  * { box-sizing: border-box; margin: 0; padding: 0; }
  html, body { width: 1200px; height: 902px; overflow: hidden; }
  body {
    background: var(--stage);
    font-family: "Source Sans 3", "Myriad Pro", sans-serif;
    position: relative;
  }
  .flyer {
    position: absolute;
    top: 153px;
    width: 420px;
    height: 596px;
    background: var(--paper);
    overflow: hidden;
  }
  .flyer--front { left: 150px; }
  .flyer--back { left: 630px; }
  .flyer__backdrop {
    position: absolute; inset: 0;
    background:
      radial-gradient(circle at 85% 12%, rgba(255,170,40,.45), transparent 18%),
      radial-gradient(circle at 65% 30%, rgba(200,90,30,.25), transparent 22%),
      radial-gradient(circle at 30% 75%, rgba(150,60,20,.22), transparent 28%),
      linear-gradient(180deg, var(--paper-glow), var(--paper) 70%);
  }
  .brand {
    position: absolute;
    display: flex; align-items: center; gap: 16px;
    color: var(--brand);
    font-weight: 700;
  }
  .brand__mark {
    flex: none;
    width: 96px; height: 96px;
    border-radius: 50%;
    background: var(--brand);
  }
  .brand__name { font-size: 30px; line-height: 1.02; }
  .flyer--front .brand { left: 40px; top: 262px; }
  .flyer--back .brand { left: 26px; top: 72px; }
  .flyer--back .brand__mark { width: 110px; height: 110px; }
  .flyer--back .brand__name { font-size: 32px; }
  .menu {
    position: absolute; left: 40px; right: 40px; top: 410px;
    border: 1px solid var(--rule);
    padding: 14px 18px;
    color: var(--accent);
    font-weight: 700; font-size: 13px; line-height: 1.5;
    text-transform: uppercase;
  }
  .menu__title { color: var(--muted); font-size: 12px; text-align: center; margin-bottom: 6px; }
  .menu__steps { list-style: none; display: grid; grid-template-columns: 1fr 1fr; column-gap: 12px; }
  .footer {
    position: absolute; left: 0; right: 0; bottom: 0;
    height: 26px;
    background: var(--footer);
    color: var(--accent);
    font-weight: 700; font-size: 11px; letter-spacing: 2.6px;
    text-transform: uppercase;
    display: flex; align-items: center; justify-content: center;
  }
  .contact {
    position: absolute; left: 22px; right: 22px; top: 242px;
    height: 223px;
    border: 1px solid var(--rule);
    color: var(--accent);
    font-weight: 700; font-size: 14.5px; line-height: 1.3;
    text-align: center; text-transform: uppercase;
    padding-top: 30px;
  }
  .contact__group + .contact__group { margin-top: 20px; }
  .pricing {
    position: absolute; left: 22px; right: 22px; top: 488px;
    text-align: center;
  }
  .pricing__title { color: var(--muted); font-weight: 700; font-size: 13px; }
  .pricing__note { color: var(--muted); font-size: 8px; margin-bottom: 16px; }
  .pricing__table {
    width: 100%; border-collapse: collapse;
    color: #b8b0ab; font-size: 7.5px; text-align: left;
  }
  .pricing__table th, .pricing__table td {
    border: 1px solid var(--table-rule);
    padding: 0 2px; font-weight: 400; line-height: 1.35;
  }
</style>
</head>
<body>
  <section class="flyer flyer--front">
    <div class="flyer__backdrop" role="img" aria-label="Dark background with warm orange out-of-focus light spots"></div>
    <div class="brand">
      <span class="brand__mark"></span>
      <span class="brand__name">Brightwell Table<br>Provisions</span>
    </div>
    <div class="menu">
      <div class="menu__title">Build your order</div>
      <ol class="menu__steps">
        <li>1. Select Glaze</li>
        <li>2. Select Sides</li>
        <li>3. Select Dessert</li>
        <li>4. Drinks</li>
      </ol>
    </div>
    <div class="footer">www.brightwelltableprovisions.com</div>
  </section>

  <section class="flyer flyer--back">
    <div class="flyer__backdrop" role="img" aria-label="Dark background with warm orange out-of-focus light spots"></div>
    <div class="brand">
      <span class="brand__mark"></span>
      <span class="brand__name">Brightwell Table<br>Provisions</span>
    </div>
    <div class="contact">
      <div class="contact__group">
        Hours of operation:<br>
        Monday - Saturday 8 AM-10 PM<br>
        Sunday 8 AM -8 PM
      </div>
      <div class="contact__group">Phone:<br>(555) 014 - 2270</div>
      <div class="contact__group">Email:<br>sales@brightwelltableprovisions.com</div>
    </div>
    <div class="pricing">
      <div class="pricing__title">AVERAGE PRICE</div>
      <div class="pricing__note">(with delivery and sides)</div>
      <table class="pricing__table">
        <tr><th>PARTY SIZE:</th><td>10</td><td>20</td><td>30</td><td>40</td><td>50</td><td>60</td><td>80</td><td>100</td><td>150</td><td>200</td></tr>
        <tr><th>PRICE:</th><td>$105</td><td>$165</td><td>$225</td><td>$290</td><td>$330</td><td>$395</td><td>$515</td><td>$625</td><td>$940</td><td>$1,235</td></tr>
      </table>
    </div>
    <div class="footer">www.brightwelltableprovisions.com</div>
  </section>
</body>
</html>
```